Annual review for The Birchmoor Collective

The Birchmoor Collective is a small public relations agency in London specialising in corporate and public affairs. Most of our work is international and we have a strong connection to South Africa. We would like to prepare a short annual review for 2016. The review will serve as both a review of our activities in 2016, and as a credentials document. Content then will include:
1. An introduction to the business
2. Who we are
3. Projects and clients undertaken in 2016
4. News and views
We imagine it will be used mostly as a pdf but would like it to be suitable for print. We envisage it to be about 8 pages long. The design look and feel should convey a business, while small, of stature. We shall include some of our client logos but we would welcome the use of some photography / imagery to have visual impact (although we don't have very much of our own!). The corporate look and feel is white, grey and black.

Industry/Entity Type

Public Relation

Font styles to use
Sans Serif

Requirements
Must have
• My project must convey a business with flair and gravitas, that punches above its weight.
Nice to have
• Thoughtful use of imagery.

```html
<!DOCTYPE html>
<html lang="en">
<head>
<meta charset="utf-8">
<title>The Birchmoor Collective – Short Annual Review 2016</title>
<link href="https://fonts.googleapis.com/css2?family=Oswald:wght@500;600&family=Open+Sans:wght@400;600&display=swap" rel="stylesheet">
<style>
  :root{
    --ink:#161616;
    --charcoal:#262626;
    --slate:#363636;
    --graphite:#444444;
    --mid-grey:#7a7a7a;
    --light-grey:#b9b9b9;
    --paper:#f4f4f4;
    --white:#ffffff;
  }
  html,body{margin:0;padding:0;overflow:hidden;background:var(--paper);}
  .spread{display:block;width:1200px;height:789px;}
  .headline{font-family:"Oswald",sans-serif;font-weight:600;fill:var(--white);letter-spacing:.5px;}
  .headline-year{font-family:"Oswald",sans-serif;font-weight:500;fill:var(--mid-grey);}
  .contact-title{font-family:"Oswald",sans-serif;font-weight:600;fill:var(--white);font-size:40px;}
  .contact-item{font-family:"Open Sans",sans-serif;font-size:14px;fill:var(--light-grey);letter-spacing:.6px;}
  .brand-name{font-family:"Open Sans",sans-serif;font-weight:600;}
  .brand-name--faint{fill:var(--mid-grey);font-size:34px;}
  .brand-name--band{fill:var(--charcoal);font-size:30px;}
  .blurb{font-family:"Open Sans",sans-serif;font-size:11px;fill:var(--light-grey);}
  .web{font-family:"Open Sans",sans-serif;font-size:14px;fill:var(--white);letter-spacing:1.2px;}
  .icon{fill:none;stroke:var(--light-grey);stroke-width:1.4;}
  .icon-solid{fill:var(--light-grey);}
</style>
</head>
<body>
<svg class="spread" viewBox="0 0 1200 789" xmlns="http://www.w3.org/2000/svg">
  <defs>
    <linearGradient id="team-photo-tone" x1="0" y1="0" x2="0" y2="1">
      <stop offset="0" stop-color="#d9d9d9"/>
      <stop offset=".55" stop-color="#8a8a8a"/>
      <stop offset="1" stop-color="#2e2e2e"/>
    </linearGradient>
    <linearGradient id="tower-photo-tone" x1="0" y1="0" x2="1" y2="1">
      <stop offset="0" stop-color="#3a3a3a"/>
      <stop offset=".45" stop-color="#9a9a9a"/>
      <stop offset="1" stop-color="#e8e8e8"/>
    </linearGradient>
  </defs>

  <!-- ===== Back cover ===== -->
  <g class="back-cover">
    <rect class="back-cover__base" x="0" y="0" width="600" height="789" fill="var(--slate)"/>
    <polygon class="back-cover__photo" role="img" aria-label="Photograph: colleagues in silhouette talking by a high window overlooking a city skyline"
             points="0,0 600,0 600,390 0,280" fill="url(#team-photo-tone)"/>
    <polygon class="back-cover__photo-rule" points="0,280 600,390 600,396 0,286" fill="var(--white)"/>
    <polygon class="back-cover__shade" points="0,500 430,789 0,789" fill="var(--charcoal)"/>
    <polygon class="back-cover__stripe" points="300,738 600,676 600,694 300,756" fill="var(--white)"/>
    <rect class="back-cover__tab" x="0" y="752" width="40" height="10" fill="var(--white)"/>

    <text class="brand-name brand-name--faint" transform="translate(95,700) rotate(-90)">The Birchmoor Collective</text>
    <circle cx="82" cy="736" r="11" fill="none" stroke="var(--mid-grey)" stroke-width="2"/>

    <text class="contact-title" x="290" y="470">CONTACT US</text>
    <g class="contact-list">
      <path class="icon-solid" d="M297 490a5 5 0 0 1 5 5c0 4-5 9-5 9s-5-5-5-9a5 5 0 0 1 5-5z"/>
      <text class="contact-item" x="314" y="502">Address Goes Here</text>
      <path class="icon" d="M292 516c1 6 5 10 11 11l2-3-3-2-2 1c-2-1-3-2-4-4l1-2-2-3z"/>
      <text class="contact-item" x="314" y="527">Phone Number Goes Here</text>
      <rect class="icon" x="291" y="542" width="12" height="9"/>
      <text class="contact-item" x="314" y="552">Fax Number Goes Here</text>
      <rect class="icon" x="291" y="567" width="12" height="9"/>
      <path class="icon" d="M291 567l6 5 6-5"/>
      <text class="contact-item" x="314" y="577">E-mail Address Goes Here</text>
    </g>

    <text class="web" x="70" y="770">www.websiteaddress.com</text>
  </g>

  <!-- ===== Front cover ===== -->
  <g class="front-cover">
    <rect class="front-cover__base" x="600" y="0" width="600" height="789" fill="var(--graphite)"/>
    <polygon class="front-cover__photo" role="img" aria-label="Photograph: looking up at glass office towers against a bright sky"
             points="600,0 1200,0 1200,110 940,560 600,560" fill="url(#tower-photo-tone)"/>

    <!-- cube facets -->
    <polygon class="cube__face cube__face--light" points="700,330 800,220 800,430" fill="#a8a8a8"/>
    <polygon class="cube__face cube__face--pale" points="700,330 800,430 760,520" fill="#e2e2e2"/>
    <polygon class="cube__face cube__face--dark" points="600,560 760,520 820,660 600,660" fill="var(--charcoal)"/>
    <polygon class="cube__outline" points="700,330 830,140 1030,180 1080,380 950,560 760,520"
             fill="none" stroke="var(--white)" stroke-width="2"/>

    <!-- title box -->
    <rect class="title-box" x="800" y="220" width="220" height="190" fill="var(--ink)" stroke="var(--white)" stroke-width="2"/>
    <text class="headline" x="910" y="275" text-anchor="middle" font-size="31">SHORT ANNUAL</text>
    <text class="headline" x="910" y="318" text-anchor="middle" font-size="39">REVIEW FOR</text>
    <text class="headline-year" x="910" y="372" text-anchor="middle" font-size="46">2016</text>

    <!-- diagonal band -->
    <polygon class="front-cover__band" points="1200,60 1200,260 963,720 860,720" fill="var(--white)"/>
    <polygon class="front-cover__band-edge" points="1200,272 1200,284 975,720 969,720" fill="var(--light-grey)"/>
    <polygon class="front-cover__foot" points="600,660 820,660 860,720 975,720 1010,789 600,789" fill="var(--charcoal)"/>
    <text class="brand-name brand-name--band" transform="translate(952,676) rotate(-62.7)">The Birchmoor Collective</text>
    <circle cx="925" cy="706" r="12" fill="none" stroke="var(--charcoal)" stroke-width="2.4"/>

    <text class="blurb" x="620" y="596">The Birchmoor Collective is a</text>
    <text class="blurb" x="620" y="611">small public relations agency</text>
    <text class="blurb" x="620" y="626">in London specialising in</text>
    <text class="blurb" x="620" y="641">corporate and public affairs.</text>

    <text class="blurb" x="1180" y="604" text-anchor="end">Most of our work is</text>
    <text class="blurb" x="1180" y="618" text-anchor="end">international and we have</text>
    <text class="blurb" x="1180" y="632" text-anchor="end">a strong connection</text>
    <text class="blurb" x="1180" y="646" text-anchor="end">to South Africa.</text>
    <rect class="front-cover__tab" x="1150" y="664" width="50" height="12" fill="var(--white)"/>

    <text class="web" x="1180" y="765" text-anchor="end">www.websiteaddress.com</text>
  </g>

  <line class="spread__fold" x1="600" y1="0" x2="600" y2="789" stroke="#1e1e1e" stroke-width="1" opacity=".5"/>
</svg>
</body>
</html>
```